https://lanternbrookpaperhouse.org/

We would like the website to represent 19th century African American civil war soldier's letters. We would like the site colors to be nice and clean . Along with the layout, including a great landing page , blogs and introduction.

```html
<!DOCTYPE html>
<html lang="en">
<head>
<meta charset="utf-8">
<title>Lanternbrook Paper House</title>
<link href="https://fonts.googleapis.com/css2?family=Almendra:wght@400;700&family=Almendra+SC&family=Roboto:wght@400;500&display=swap" rel="stylesheet">
<style>
:root{
  --parchment:#ecd7ad;
  --parchment-light:#f6ead2;
  --parchment-dark:#d4a96a;
  --parchment-deep:#c89658;
  --brown-dark:#5b2c12;
  --brown-mid:#7a3d18;
  --brown-active:#8c5e40;
  --heading:#6a2e10;
  --wood:#d98a42;
  --wood-dark:#b86a28;
  --ink:#333333;
  --muted:#7c7c7c;
  --meta-ico:#c98a4a;
  --footer:#2b2b2b;
  --white:#ffffff;
}
*{box-sizing:border-box;margin:0;padding:0}
html,body{width:1200px;height:3765px;overflow:hidden}
body{
  position:relative;
  font-family:"Roboto",sans-serif;
  color:var(--ink);
  background:
    radial-gradient(ellipse 480px 1500px at 600px 1900px,rgba(246,234,210,.95) 0%,rgba(246,234,210,0) 100%),
    radial-gradient(ellipse 420px 260px at 600px 850px,rgba(246,234,210,.9) 0%,rgba(246,234,210,0) 100%),
    radial-gradient(ellipse 160px 120px at 90px 180px,rgba(200,150,88,.7) 0%,rgba(200,150,88,0) 100%),
    radial-gradient(ellipse 140px 220px at 60px 620px,rgba(200,150,88,.75) 0%,rgba(200,150,88,0) 100%),
    radial-gradient(ellipse 120px 300px at 40px 1300px,rgba(200,150,88,.8) 0%,rgba(200,150,88,0) 100%),
    radial-gradient(ellipse 170px 260px at 70px 2050px,rgba(200,150,88,.75) 0%,rgba(200,150,88,0) 100%),
    radial-gradient(ellipse 150px 320px at 50px 2800px,rgba(200,150,88,.8) 0%,rgba(200,150,88,0) 100%),
    radial-gradient(ellipse 180px 240px at 80px 3550px,rgba(200,150,88,.75) 0%,rgba(200,150,88,0) 100%),
    radial-gradient(ellipse 150px 160px at 1120px 120px,rgba(200,150,88,.7) 0%,rgba(200,150,88,0) 100%),
    radial-gradient(ellipse 130px 280px at 1160px 900px,rgba(200,150,88,.7) 0%,rgba(200,150,88,0) 100%),
    radial-gradient(ellipse 160px 300px at 1150px 1650px,rgba(200,150,88,.75) 0%,rgba(200,150,88,0) 100%),
    radial-gradient(ellipse 140px 320px at 1160px 2450px,rgba(200,150,88,.8) 0%,rgba(200,150,88,0) 100%),
    radial-gradient(ellipse 170px 260px at 1130px 3250px,rgba(200,150,88,.75) 0%,rgba(200,150,88,0) 100%),
    radial-gradient(ellipse 260px 90px at 420px 1500px,rgba(212,169,106,.55) 0%,rgba(212,169,106,0) 100%),
    radial-gradient(ellipse 260px 90px at 800px 3310px,rgba(212,169,106,.55) 0%,rgba(212,169,106,0) 100%),
    linear-gradient(90deg,var(--parchment-dark) 0%,var(--parchment) 12%,var(--parchment) 88%,var(--parchment-dark) 100%);
}
.abs{position:absolute}

/* header */
.brand{left:444px;top:7px;display:flex;align-items:center;gap:14px}
.brand-mark{width:93px;height:93px;border-radius:50%;background:var(--brown-mid)}
.brand-name{font-family:"Almendra",serif;font-size:27px;line-height:30px;color:var(--brown-dark)}

.nav{left:143px;top:120px;width:912px;height:61px;background:var(--brown-dark);display:flex;align-items:center}
.nav a{color:var(--white);text-decoration:none;font-size:16px;font-weight:500;padding:0 19px;height:61px;line-height:61px}
.nav a.active{background:var(--brown-active);padding:0 25px 0 40px}
.search{position:absolute;left:589px;top:14px;width:301px;height:33px;background:var(--parchment-light);display:flex;align-items:center;justify-content:space-between;padding:0 14px;font-size:12px;color:#555}

/* hero */
.hero{left:143px;top:181px;width:912px;height:440px;background:linear-gradient(135deg,#6b4a2e 0%,#9c7a56 45%,#c9a97e 70%,#8a5a36 100%)}
.hero-tear{left:0;bottom:-1px}
.hero-caption{left:176px;top:126px;width:562px;height:153px;background:rgba(38,30,26,.92);color:var(--white);font-family:"Almendra SC",serif;font-size:34px;line-height:41px;text-align:center;display:flex;align-items:center;justify-content:center;letter-spacing:1px}
.hero-arrow{width:48px;height:48px;border-radius:50%;background:rgba(30,22,18,.8);top:178px}
.dots{left:420px;top:389px;display:flex;gap:6px}
.dots span{width:9px;height:9px;border-radius:50%;background:#fff}
.dots span.on{background:var(--brown-dark)}

/* about */
.section-title{font-family:"Almendra SC",serif;font-size:46px;color:var(--heading);letter-spacing:1px;font-weight:400}
.about-text{left:143px;top:770px;width:420px;font-size:14.5px;line-height:29px;color:#555}
.btn{display:inline-block;width:160px;height:47px;line-height:47px;text-align:center;background:linear-gradient(180deg,#e6a15b 0%,var(--wood) 55%,var(--wood-dark) 100%);color:var(--heading);font-family:"Almendra SC",serif;font-size:18px;border-radius:3px;box-shadow:0 4px 5px rgba(70,30,10,.35)}
.portrait{left:610px;top:668px;width:440px;height:410px;border-radius:48% 52% 46% 54%/50% 48% 52% 50%;background:radial-gradient(circle at 50% 50%,#b9a79a 0%,#6b5a52 55%,#2a2220 100%)}

/* banner */
.banner{left:143px;top:1158px;width:912px;height:289px;background:radial-gradient(ellipse at 50% 40%,#7a3d16 0%,#4f220b 100%);color:var(--parchment-light);font-family:"Almendra",serif;font-size:52px;line-height:62px;text-align:center;display:flex;align-items:center;justify-content:center}
.banner-ground{left:0;bottom:0;width:912px;height:36px;background:var(--parchment-dark)}

/* blog cards */
.card{left:143px;width:912px;height:400px;background:var(--white);display:flex}
.card-img{width:391px;height:400px;flex:none}
.card-body{flex:1;padding:50px 46px 0 46px;position:relative}
.card-title{font-size:24px;line-height:34px;color:#333;font-weight:400;width:360px}
.meta{margin-top:24px;font-size:11.5px;color:#333;display:flex;align-items:center;gap:6px}
.meta i{display:inline-block;width:8px;height:8px;background:var(--meta-ico);border-radius:50%}
.meta .sep{color:#999}
.excerpt{margin-top:24px;font-size:13px;line-height:26px;color:var(--muted);width:425px}
.card .btn{margin-top:26px}

.pager{left:462px;top:3330px;display:flex;gap:7px}
.pager span{width:40px;height:40px;border-radius:50%;border:2px solid var(--brown-dark);color:var(--brown-dark);font-size:18px;font-weight:500;display:flex;align-items:center;justify-content:center}
.pager span.on{background:var(--brown-dark);color:var(--white)}

/* footer */
.footer{left:143px;top:3457px;width:912px;height:215px;background:var(--footer);color:var(--white);text-align:center}
.footer-menu{margin-top:46px;font-size:22px;font-weight:500;word-spacing:6px}
.copy{margin-top:18px;font-size:12px}
.social{margin-top:17px;display:flex;justify-content:center;gap:7px}
.social span{width:37px;height:37px;border-radius:50%;border:2px solid var(--white);font-size:9px;font-weight:500;color:var(--white);display:flex;align-items:center;justify-content:center}
.page-code{right:38px;top:3742px;font-size:13px;color:#222}
</style>
</head>
<body>

<header>
  <div class="abs brand">
    <div class="brand-mark"></div>
    <div class="brand-name">Lanternbrook<br>Paper House</div>
  </div>
  <nav class="abs nav">
    <a class="active" href="#">HOME</a>
    <a href="#">ABOUT</a>
    <a href="#">BLOG</a>
    <a href="#">CONTACT</a>
    <a href="#">BLOG</a>
    <div class="search"><span>Search</span>
      <svg width="12" height="12" viewBox="0 0 12 12"><circle cx="5" cy="5" r="3.6" fill="none" stroke="#333" stroke-width="1.6"/><line x1="7.6" y1="7.6" x2="11" y2="11" stroke="#333" stroke-width="1.6"/></svg>
    </div>
  </nav>
</header>

<section class="abs hero" role="img" aria-label="Desk with quill, sealed letters, candle and coffee cup">
  <div class="abs hero-caption">EXPLORING THE LIVES AND<br>LETTERS OF MEN WHO<br>SERVED IN THE USCT</div>
  <div class="abs hero-arrow" style="left:33px"><svg width="48" height="48" viewBox="0 0 48 48"><polyline points="27,16 19,24 27,32" fill="none" stroke="#fff" stroke-width="2.4"/></svg></div>
  <div class="abs hero-arrow" style="left:831px"><svg width="48" height="48" viewBox="0 0 48 48"><polyline points="21,16 29,24 21,32" fill="none" stroke="#fff" stroke-width="2.4"/></svg></div>
  <div class="abs dots"><span></span><span></span><span class="on"></span><span></span><span></span></div>
  <svg class="abs hero-tear" width="912" height="18" viewBox="0 0 912 18" preserveAspectRatio="none"><polygon fill="#ecd7ad" points="0,18 0,10 35,14 80,6 130,12 190,4 250,11 310,7 370,13 430,5 500,12 560,6 620,13 690,4 750,11 810,6 870,12 912,8 912,18"/></svg>
</section>

<section>
  <h2 class="abs section-title" style="left:143px;top:696px">ABOUT</h2>
  <p class="abs about-text">Dana Whitfield Morrow is a Virginia native and Maryland-based researcher and scholar. She has received her Ph.D. in English Literature from Halden Ridge University, her M.A. in English Literature from Coastal Plains University, and her B.A. in Mass Media Arts from Tidewater College. Her areas of specialization include African American Epistolary Literature, African American Civil War letters,</p>
  <a class="abs btn" style="left:145px;top:996px">READ MORE</a>
  <div class="abs portrait" role="img" aria-label="Portrait of the author with painted brush edge"></div>
</section>

<section class="abs banner" role="img" aria-label="Banner with soldier silhouettes and site name">
  <div class="abs banner-ground"></div>
  <span style="position:relative">Lanternbrook<br>Paper House</span>
</section>

<section>
  <h2 class="abs section-title" style="left:143px;top:1518px">LATEST BLOGS</h2>

  <article class="abs card" style="top:1605px">
    <div class="card-img" role="img" aria-label="Aged paper with inkwell on a wooden desk" style="background:linear-gradient(135deg,#6b3a1e 0%,#c9a677 40%,#e0c79d 70%,#7a4422 100%)"></div>
    <div class="card-body">
      <h3 class="card-title">I'm well and doing well as a soldier can expect...</h3>
      <div class="meta"><i></i>By dwmorrow <span class="sep">|</span><i></i>February 16, 2020 <span class="sep">|</span><i></i>No Comments <span class="sep">|</span><i></i>Sticky post</div>
      <p class="excerpt">Hollis's ninth letter in this collection was written December 29th, 1864 while he and his regiment were in Beaufort, South Carolina.His letter opens with acknowledging the receipt of his mother's last letter. We also find that Hollis has made good on his promise.</p>
      <a class="btn">READ MORE</a>
    </div>
  </article>

  <article class="abs card" style="top:2026px">
    <div class="card-body">
      <h3 class="card-title">Lorem ipsum dolor sit ameconse ctetued do eiusmod tempor</h3>
      <div class="meta"><i></i>By dwmorrow <span class="sep">|</span><i></i>February 16, 2020 <span class="sep">|</span><i></i>No Comments <span class="sep">|</span><i></i>Sticky post</div>
      <p class="excerpt">Hollis's ninth letter in this collection was written December 29th, 1864 while he and his regiment were in Beaufort, South Carolina.His letter opens with acknowledging the receipt of his mother's last letter. We also find that Hollis has made good on his promise.</p>
      <a class="btn">READ MORE</a>
    </div>
    <div class="card-img" role="img" aria-label="Old express shipping receipts and tags on a table" style="background:linear-gradient(135deg,#e8e2da 0%,#d7cdc2 40%,#c9793a 75%,#5a3a22 100%)"></div>
  </article>

  <article class="abs card" style="top:2450px">
    <div class="card-img" role="img" aria-label="Handwritten letter from 1864" style="background:linear-gradient(135deg,#d8d8d8 0%,#eeeeee 50%,#cfcfcf 100%)"></div>
    <div class="card-body">
      <h3 class="card-title">Sed ut perspiciatis unde omnis iste natus eluptatem</h3>
      <div class="meta"><i></i>By dwmorrow <span class="sep">|</span><i></i>February 16, 2020 <span class="sep">|</span><i></i>No Comments <span class="sep">|</span><i></i>Sticky post</div>
      <p class="excerpt">Hollis's ninth letter in this collection was written December 29th, 1864 while he and his regiment were in Beaufort, South Carolina.His letter opens with acknowledging the receipt of his mother's last letter. We also find that Hollis has made good on his promise.</p>
      <a class="btn">READ MORE</a>
    </div>
  </article>

  <article class="abs card" style="top:2872px">
    <div class="card-body">
      <h3 class="card-title">Prspiciatis unde omnis isteatus error sitccusantium doloremque</h3>
      <div class="meta"><i></i>By dwmorrow <span class="sep">|</span><i></i>February 16, 2020 <span class="sep">|</span><i></i>No Comments <span class="sep">|</span><i></i>Sticky post</div>
      <p class="excerpt">Hollis's ninth letter in this collection was written December 29th, 1864 while he and his regiment were in Beaufort, South Carolina.His letter opens with acknowledging the receipt of his mother's last letter. We also find that Hollis has made good on his promise.</p>
      <a class="btn">READ MORE</a>
    </div>
    <div class="card-img" role="img" aria-label="Research desk with laptop, glasses and archive documents" style="background:linear-gradient(135deg,#3a2a1c 0%,#8a6a40 45%,#b08a58 65%,#4a3420 100%)"></div>
  </article>
</section>

<nav class="abs pager">
  <span>&laquo;</span><span class="on">1</span><span>2</span><span>3</span><span>4</span><span>&raquo;</span>
</nav>

<footer class="abs footer">
  <svg class="abs" style="left:0;top:-8px" width="912" height="12" viewBox="0 0 912 12" preserveAspectRatio="none"><polygon fill="#2b2b2b" points="0,12 0,5 40,8 90,3 150,7 210,2 280,6 340,3 410,8 470,2 540,6 600,3 660,8 730,4 790,7 850,2 912,6 912,12"/></svg>
  <div class="footer-menu">HOME &nbsp;/ &nbsp;ABOUT &nbsp;/ &nbsp;BLOG &nbsp;/ &nbsp;CONTACT &nbsp;/ &nbsp;BLOG</div>
  <p class="copy">Copyright © 2020 Lanternbrook Paper House . All Rights Reserved</p>
  <div class="social"><span>Ripl</span><span>Chrp</span><span>Lnkr</span><span>Reel</span></div>
</footer>

<div class="abs page-code">C9</div>
</body>
</html>
```